QTVlink PowerPoint Template with existing Logo and Letterhead template

Develop a PowerPoint template based on existing logo and letterhead designs for a Marketing Consultancy.
Presentations that will be made with title slide, content slides (which includes mostly bullet point text and some tables) and also last page company introduction and copyright.
Corporate colors should be keep as per the logo

I like something like from Pixel Harbor
- Serious, Modern PowerPoint Design for Company in Canada | Design 418674
- Professional, Modern PowerPoint Design for Company in United States | Design 7795293
- Professional, Modern PowerPoint Design for Company in United States | Design 7826742
- Serious, Modern PowerPoint Design for Company in Canada | Design 418635
- Elegant, Serious PowerPoint Design for Company in Puerto Rico | Design 16951178
- Bold, Modern PowerPoint Design for Company in United States | Design 11745238

To all designers, • We need sleek and modern looking PowerPoint presentation template. • The template will primarily be used for our corporate slide and solutions presentation for our customers. • Not too much of white and it should be sleek, modern and impressive for marketing consultancy firms like us. • Please ensure the content pages are water marketed with the 4 boxes. • I like something like from Pixel Harbor and you can get some idea on what I like.: o Serious, Modern PowerPoint Design for Company in Canada | Design 418674 o Professional, Modern PowerPoint Design for Company in United States | Design 7795293 o Professional, Modern PowerPoint Design for Company in United States | Design 7826742 o Serious, Modern PowerPoint Design for Company in Canada | Design 418635 o Elegant, Serious PowerPoint Design for Company in Puerto Rico | Design 16951178 o Bold, Modern PowerPoint Design for Company in United States | Design 11745238 Thanks!

Target Market(s)

Marketing Managers, B2B Marketing Team, CRM Data Owners

Industry/Entity Type

Marketing

Requirements
Must have
• Not too much of white and it should be sleek, modern and impressive for marketing consultancy firms like us. Please ensure the content pages are water marketed with the 4 boxes. The template will primarily be used for our corporate slides and solutions presentation for our customers.
Should not have
• no background in the slide content area

```html
<!DOCTYPE html>
<html lang="en">
<head>
<meta charset="utf-8">
<title>QTVlink Presentation Template</title>
<link href="https://fonts.googleapis.com/css2?family=Montserrat:wght@300;400;500;600;700&display=swap" rel="stylesheet">
<style>
:root{
  --red:#e8202a;
  --navy:#56607a;
  --navy-dark:#454e66;
  --ink:#333;
  --grey:#6b6b6b;
  --text:#777;
  --light:#bdbdbd;
  --paper:#fff;
}
*{box-sizing:border-box;margin:0;padding:0}
html,body{width:1200px;height:1152px;overflow:hidden;background:#fff}
body{font-family:'Montserrat',sans-serif;color:var(--text)}
.board{position:relative;width:1460px;height:1402px;transform:scale(0.8219);transform-origin:0 0}
.slide{position:absolute;width:478px;height:268px;background:var(--paper);overflow:hidden;box-shadow:0 1px 4px rgba(0,0,0,.25)}
.c1{left:4px}.c2{left:490px}.c3{left:976px}
.r1{top:10px}.r2{top:292px}.r3{top:574px}.r4{top:856px}.r5{top:1138px}
.abs{position:absolute}
.title{position:absolute;left:20px;top:18px;font-size:16px;font-weight:300;color:#555}
.title::after{content:"";position:absolute;left:0;top:26px;width:24px;height:2px;background:var(--red)}
.brand{position:absolute;right:14px;top:18px;font-size:13px;font-weight:700;color:var(--red);letter-spacing:.5px;display:flex;align-items:center;gap:4px}
.brand i{width:6px;height:6px;background:var(--navy);display:block}
.foot{position:absolute;left:0;bottom:0;width:100%;height:12px;background:var(--navy);color:#fff;font-size:5px;line-height:12px;padding-left:20px}
.pg{position:absolute;right:26px;bottom:0;width:14px;height:14px;background:var(--red);color:#fff;font-size:5px;text-align:center;line-height:14px}
.tiny{font-size:6px;line-height:1.35;color:#999}
.photo{position:absolute}
.ico{position:absolute;border-radius:50%;display:flex;align-items:center;justify-content:center}
.ico svg{width:55%;height:55%}
</style>
</head>
<body>
<div class="board">

<section class="slide c1 r1">
  <div class="photo" role="img" aria-label="Black and white photo of a modern glass office building" style="left:0;top:0;width:335px;height:268px;background:linear-gradient(135deg,#e8e8e8,#9a9a9a 55%,#d6d6d6)"></div>
  <div class="abs" style="left:239px;top:62px;width:239px;height:152px;background:#ef4b50;padding:28px 24px 0 25px;color:#fff">
    <h2 style="font-size:16px;font-weight:400">About Us</h2>
    <div style="width:24px;height:2px;background:#fff;margin:6px 0 10px"></div>
    <p style="font-size:7.2px;line-height:1.3">Lorem ipsum dolor sit amet, consectetur adipiscing elit, sed do eiusmod tempor incididunt ut labore et dolore magna aliqua.</p>
    <p style="font-size:7.2px;line-height:1.3;margin-top:6px">Ut enimad minim veniam, quis nostrud exercitation ullamco laboris nisi ut aliquip ex ea commodo consequat.</p>
  </div>
</section>

<section class="slide c2 r1" style="background:linear-gradient(160deg,#5e6882,#4b556e)">
  <div class="brand" style="top:16px">QTVlink<i style="background:#fff"></i></div>
  <h1 class="abs" style="left:30px;top:174px;font-size:24px;font-weight:700;color:#fff"><span style="color:var(--red)">This Is Your</span> Divider Page</h1>
  <p class="abs" style="left:30px;top:208px;font-size:8px;color:var(--red)">Your Sub Title Goes Here</p>
</section>

<section class="slide c3 r1">
  <h2 class="title">Quote Area</h2>
  <div class="brand">QTVlink<i></i></div>
  <div class="abs" style="left:0;top:58px;width:478px;height:168px;background:var(--navy)"></div>
  <div class="photo" role="img" aria-label="City skyline photographed at sunset" style="left:239px;top:58px;width:239px;height:168px;background:linear-gradient(160deg,#3a3a3a,#b06b2e 55%,#e8a44c)"></div>
  <blockquote class="abs" style="left:24px;top:104px;color:#fff;font-size:12px;line-height:1.2;font-weight:300">“ Coming together is a beginning.<br>&nbsp;&nbsp;Keeping together is progress.<br>&nbsp;&nbsp;Working together is success.”<br><br>&nbsp;&nbsp;- Walter Brandt -</blockquote>
  <div class="foot">© Copyright 2017 QTVlink. All rights reserved.</div><div class="pg">21</div>
</section>

<section class="slide c1 r2">
  <h2 class="title">Brand Detailed</h2>
  <div class="brand">QTVlink<i></i></div>
  <div class="photo" role="img" aria-label="Hands typing on a laptop showing a photo gallery" style="left:32px;top:66px;width:219px;height:171px;background:linear-gradient(135deg,#c9c4bf,#6d6a68 60%,#3d3b3a)"></div>
  <div class="abs" style="left:255px;top:66px;width:91px;height:83px;background:var(--red);color:#fff;text-align:center;padding-top:16px;font-size:6.5px;line-height:1.2"><b style="font-size:7.5px">System</b><br>Mauris quam dolor, cursus at porta et, luctus eget purus. Nunc tempor luctus interdum.</div>
  <div class="abs" style="left:351px;top:66px;width:91px;height:83px;background:var(--navy);color:#fff;text-align:center;padding-top:16px;font-size:6.5px;line-height:1.2"><b style="font-size:7.5px">Technology</b><br>Mauris quam dolor, cursus at porta et, luctus eget purus. Nunc tempor luctus interdum.</div>
  <div class="abs" style="left:255px;top:154px;width:91px;height:83px;background:var(--ink);color:#fff;text-align:center;padding-top:16px;font-size:6.5px;line-height:1.2"><b style="font-size:7.5px">Leisure</b><br>Mauris quam dolor, cursus at porta et, luctus eget purus. Nunc tempor luctus interdum.</div>
  <div class="abs" style="left:351px;top:154px;width:91px;height:83px;background:var(--grey);color:#fff;text-align:center;padding-top:16px;font-size:6.5px;line-height:1.2"><b style="font-size:7.5px">Digital</b><br>Mauris quam dolor, cursus at porta et, luctus eget purus. Nunc tempor luctus interdum.</div>
  <div class="foot">© Copyright 2017 QTVlink. All rights reserved.</div><div class="pg">22</div>
</section>

<section class="slide c2 r2">
  <h2 class="title">Product Philosophy</h2>
  <div class="brand">QTVlink<i></i></div>
  <svg class="abs" style="left:176px;top:88px" width="128" height="128" viewBox="0 0 128 128">
    <g transform="rotate(-90 64 64)" fill="none" stroke-width="32">
      <circle cx="64" cy="64" r="46" stroke="var(--navy)" stroke-dasharray="43.35 289"/>
      <circle cx="64" cy="64" r="46" stroke="var(--ink)" stroke-dasharray="0 43.35 72.26 289"/>
      <circle cx="64" cy="64" r="46" stroke="var(--grey)" stroke-dasharray="0 115.61 57.8 289"/>
      <circle cx="64" cy="64" r="46" stroke="var(--red)" stroke-dasharray="0 173.41 115.61 289"/>
    </g>
    <circle cx="64" cy="64" r="30" fill="#fff"/>
    <g fill="#fff" font-size="8" font-family="Montserrat,sans-serif" text-anchor="middle"><text x="84" y="36">15%</text><text x="106" y="70">25%</text><text x="62" y="115">20%</text><text x="16" y="68">40%</text></g>
  </svg>
  <div class="ico" style="left:120px;top:74px;width:44px;height:44px;background:var(--red)"><svg viewBox="0 0 24 24" fill="none" stroke="#fff" stroke-width="1.5"><circle cx="12" cy="12" r="8"/><circle cx="12" cy="12" r="3"/></svg></div>
  <div class="ico" style="left:120px;top:181px;width:44px;height:44px;background:var(--grey)"><svg viewBox="0 0 24 24" fill="none" stroke="#fff" stroke-width="1.5"><path d="M12 4a6 6 0 0 0-3 11v3h6v-3a6 6 0 0 0-3-11z"/></svg></div>
  <div class="ico" style="left:318px;top:74px;width:44px;height:44px;background:var(--navy)"><svg viewBox="0 0 24 24" fill="none" stroke="#fff" stroke-width="1.5"><circle cx="12" cy="12" r="8"/><circle cx="9" cy="10" r="2"/><circle cx="15" cy="15" r="2"/></svg></div>
  <div class="ico" style="left:318px;top:181px;width:44px;height:44px;background:var(--ink)"><svg viewBox="0 0 24 24" fill="none" stroke="#fff" stroke-width="1.5"><rect x="5" y="6" width="14" height="12"/><path d="M8 10h8M8 14h5"/></svg></div>
  <div class="abs tiny" style="right:364px;top:76px;text-align:right;width:90px"><span style="color:var(--red);font-size:7px">Secure</span><br>Nullam eu tempor purus. Nunc a leo magna, sit amet consequat risus.</div>
  <div class="abs tiny" style="right:364px;top:186px;text-align:right;width:90px"><span style="color:#666;font-size:7px">Good Package</span><br>Nullam eu tempor purus. Nunc a leo magna, sit amet consequat risus.</div>
  <div class="abs tiny" style="left:369px;top:76px;width:90px"><span style="color:#666;font-size:7px">Well Organized</span><br>Nullam eu tempor purus. Nunc a leo magna, sit amet consequat risus.</div>
  <div class="abs tiny" style="left:369px;top:186px;width:90px"><span style="color:#666;font-size:7px">Publication</span><br>Nullam eu tempor purus. Nunc a leo magna, sit amet consequat risus.</div>
  <div class="foot">© Copyright 2017 QTVlink. All rights reserved.</div><div class="pg">23</div>
</section>

<section class="slide c3 r2">
  <div class="photo" role="img" aria-label="Faded grey city skyline" style="left:0;top:0;width:478px;height:190px;background:linear-gradient(180deg,#f4f4f4,#d9d9d9)"></div>
  <div class="abs" style="left:222px;top:41px;font-size:5px;color:#555"><span style="color:var(--red)">■</span> 2018 &nbsp;<span style="color:var(--ink)">■</span> 2019</div>
  <svg class="abs" style="left:0;top:0" width="478" height="190" font-family="Montserrat,sans-serif" font-size="8" fill="#333" text-anchor="middle">
    <rect x="52" y="111" width="28" height="72" fill="var(--red)"/><rect x="87" y="93" width="28" height="90" fill="var(--ink)"/>
    <text x="66" y="106">400</text><text x="101" y="88">500</text>
    <rect x="157" y="129" width="28" height="54" fill="var(--red)"/><rect x="193" y="75" width="28" height="108" fill="var(--ink)"/>
    <text x="171" y="124">300</text><text x="207" y="70">600</text>
    <rect x="263" y="131" width="28" height="52" fill="var(--red)"/><rect x="297" y="147" width="28" height="36" fill="var(--ink)"/>
    <text x="277" y="126">290</text><text x="311" y="142">200</text>
    <rect x="370" y="147" width="28" height="36" fill="var(--red)"/><rect x="405" y="165" width="28" height="18" fill="var(--ink)"/>
    <text x="384" y="142">200</text><text x="419" y="160">100</text>
  </svg>
  <div class="abs" style="left:0;top:190px;width:478px;height:78px;background:var(--navy);display:flex;padding:14px 20px 0;color:#fff;text-align:center">
    <div style="flex:1;font-size:5px;line-height:1.25"><b style="font-size:7px">Asia</b><br>Duis quis purus adipiscing mi scelerisque dictum quis vel eros. Nullam eu tempor purus.</div>
    <div style="flex:1;font-size:5px;line-height:1.25"><b style="font-size:7px">Africa</b><br>Duis quis purus adipiscing mi scelerisque dictum quis vel eros. Nullam eu tempor purus.</div>
    <div style="flex:1;font-size:5px;line-height:1.25"><b style="font-size:7px">America</b><br>Duis quis purus adipiscing mi scelerisque dictum quis vel eros. Nullam eu tempor purus.</div>
    <div style="flex:1;font-size:5px;line-height:1.25"><b style="font-size:7px">Euro</b><br>Duis quis purus adipiscing mi scelerisque dictum quis vel eros. Nullam eu tempor purus.</div>
  </div>
</section>

<section class="slide c1 r3">
  <h2 class="title">Trending In The World</h2>
  <div class="brand">QTVlink<i></i></div>
  <div class="photo" role="img" aria-label="Grey world map" style="left:20px;top:62px;width:300px;height:178px;background:radial-gradient(ellipse at 50% 45%,#cfcfcf,#e6e6e6 70%,#fff 100%)"></div>
  <div class="ico" style="left:38px;top:126px;width:36px;height:36px;background:rgba(232,32,42,.85);color:#fff;font-size:12px">25%</div>
  <div class="ico" style="left:124px;top:104px;width:50px;height:50px;background:rgba(110,110,110,.85);color:#fff;font-size:16px">80%</div>
  <div class="ico" style="left:258px;top:112px;width:52px;height:52px;background:rgba(120,120,120,.8);color:#fff;font-size:16px">75%</div>
  <div class="ico" style="left:216px;top:160px;width:32px;height:32px;background:rgba(70,70,70,.85);color:#fff;font-size:10px">15%</div>
  <div class="ico" style="left:334px;top:80px;width:36px;height:36px;border:2px solid var(--red);background:#fff"><svg viewBox="0 0 24 24" fill="var(--red)"><rect x="7" y="5" width="10" height="14"/></svg></div>
  <div class="ico" style="left:334px;top:130px;width:36px;height:36px;border:2px solid #777;background:#fff"><svg viewBox="0 0 24 24" fill="none" stroke="#555" stroke-width="1.8"><path d="M8 18V9M11 18V6M14 18V7M17 18v-7"/></svg></div>
  <div class="ico" style="left:334px;top:180px;width:36px;height:36px;border:2px solid #777;background:#fff"><svg viewBox="0 0 24 24" fill="#555"><rect x="6" y="12" width="3" height="7"/><rect x="10.5" y="8" width="3" height="11"/><rect x="15" y="10" width="3" height="9"/></svg></div>
  <div class="abs tiny" style="left:374px;top:80px;width:90px"><span style="color:var(--red);font-size:7px">Confusion</span><br>Nullam eu tempor purus. Nunc a leo magna, sit amet consequat risus.</div>
  <div class="abs tiny" style="left:374px;top:130px;width:90px"><span style="color:#666;font-size:7px">Intangible</span><br>Nullam eu tempor purus. Nunc a leo magna, sit amet consequat risus.</div>
  <div class="abs tiny" style="left:374px;top:180px;width:90px"><span style="color:#666;font-size:7px">Performance</span><br>Nullam eu tempor purus. Nunc a leo magna, sit amet consequat risus.</div>
  <div class="foot">© Copyright 2017 QTVlink. All rights reserved.</div><div class="pg">25</div>
</section>

<section class="slide c2 r3">
  <h2 class="title">Our Vision &amp; Mission</h2>
  <div class="brand">QTVlink<i></i></div>
  <div class="abs" style="left:0;top:52px;width:478px;height:173px;background:linear-gradient(180deg,#5a647d,#4a546c)"></div>
  <div class="abs" style="left:24px;top:78px;width:210px;color:#fff">
    <p style="font-size:12px;font-weight:300">▪ Our Vision:</p>
    <p style="font-size:10px;font-weight:600;line-height:1.25;margin:6px 0 0 8px">Go to the Next Level<br>Without look in the past</p>
    <div style="width:44px;height:1px;background:#fff;margin:9px 0 8px 8px"></div>
    <p style="font-size:6px;line-height:1.3;margin-left:8px">Lorem ipsum dolor sit amet, consectetur adipiscing elit, sed do eiusmod tempor incididunt ut labore et dolore magna aliqua. Ut enim ad minim veniam, quis nostrud exercitation ullamco laboris nisi ut aliquip ex ea commodo consequat.</p>
  </div>
  <div class="abs" style="left:266px;top:78px;width:200px;color:#fff">
    <p style="font-size:12px;font-weight:300">▪ Our Missions:</p>
    <div style="display:flex;gap:10px;margin-top:8px"><span style="width:22px;height:22px;border-radius:50%;background:#fff;flex:none;display:flex;align-items:center;justify-content:center"><span style="width:8px;height:8px;border-radius:50%;background:var(--red)"></span></span><div><p style="font-size:10px">Your Text Here</p><p style="font-size:5.5px;line-height:1.3">Lorem ipsum dolor sit consectetur adipiscing elit, sed do eiusmod tempo.</p></div></div>
    <div style="display:flex;gap:10px;margin-top:6px"><span style="width:22px;height:22px;border-radius:50%;background:#fff;flex:none;display:flex;align-items:center;justify-content:center"><span style="width:8px;height:8px;border-radius:50%;background:var(--red)"></span></span><div><p style="font-size:10px">Your Text Here</p><p style="font-size:5.5px;line-height:1.3">Lorem ipsum dolor sit consectetur adipiscing elit, sed do eiusmod tempo.</p></div></div>
    <div style="display:flex;gap:10px;margin-top:6px"><span style="width:22px;height:22px;border-radius:50%;background:#fff;flex:none;display:flex;align-items:center;justify-content:center"><span style="width:8px;height:8px;border-radius:50%;background:var(--red)"></span></span><div><p style="font-size:10px">Your Text Here</p><p style="font-size:5.5px;line-height:1.3">Lorem ipsum dolor sit consectetur adipiscing elit, sed do eiusmod tempo.</p></div></div>
  </div>
  <div class="foot">© Copyright 2017 QTVlink. All rights reserved.</div><div class="pg">26</div>
</section>

<section class="slide c3 r3">
  <h2 class="title">Our Services</h2>
  <div class="brand">QTVlink<i></i></div>
  <div class="photo" role="img" aria-label="Glowing blue circuit board pattern" style="left:44px;top:60px;width:186px;height:117px;background:radial-gradient(circle at 45% 50%,#3d6fa8,#14213a 60%,#0b1424)"></div>
  <p class="abs" style="left:44px;top:186px;font-size:9px;color:var(--red)">Your Title Goes Here</p>
  <p class="abs tiny" style="left:44px;top:198px;width:200px;font-size:5.5px">Lorem ipsum dolor sit amet, sed do eiusmod tempor incididunt ut labore et dolore magna aliqua. Ut enimad minim veniam, quis nostrud exercitation ullamco laboris nisi ut aliquip ex ea commodo consequat.</p>
  <div class="ico" style="left:260px;top:62px;width:22px;height:22px;background:var(--red)"><svg viewBox="0 0 24 24" fill="#fff"><rect x="6" y="12" width="3" height="6"/><rect x="11" y="8" width="3" height="10"/><rect x="16" y="10" width="3" height="8"/></svg></div>
  <div class="ico" style="left:260px;top:118px;width:22px;height:22px;background:var(--navy)"><svg viewBox="0 0 24 24" fill="none" stroke="#fff" stroke-width="2"><path d="M7 17l10-10M10 7h7v7"/></svg></div>
  <div class="ico" style="left:260px;top:174px;width:22px;height:22px;background:var(--ink)"><svg viewBox="0 0 24 24" fill="none" stroke="#fff" stroke-width="2"><circle cx="11" cy="11" r="5"/><path d="M15 15l4 4"/></svg></div>
  <div class="abs" style="left:295px;top:60px;width:170px"><p style="font-size:9.5px;color:var(--red)">Service Number One</p><p class="tiny" style="font-size:5.5px">Lorem ipsum dolor sit amer, consectetur adipiscing elit, sed do eiusmod tempor incididunt ut labore et dolore magna aliqua.</p></div>
  <div class="abs" style="left:295px;top:117px;width:170px"><p style="font-size:9.5px;color:#555">Service Number Two</p><p class="tiny" style="font-size:5.5px">Lorem ipsum dolor sit amer, consectetur adipiscing elit, sed do eiusmod tempor incididunt ut labore et dolore magna aliqua.</p></div>
  <div class="abs" style="left:295px;top:174px;width:170px"><p style="font-size:9.5px;color:#555">Service Number Three</p><p class="tiny" style="font-size:5.5px">Lorem ipsum dolor sit amer, consectetur adipiscing elit, sed do eiusmod tempor incididunt ut labore et dolore magna aliqua.</p></div>
  <div class="foot">© Copyright 2017 QTVlink. All rights reserved.</div><div class="pg">27</div>
</section>

<section class="slide c1 r4">
  <h2 class="title">Three Column Description</h2>
  <div class="brand">QTVlink<i></i></div>
  <p class="abs" style="left:25px;top:64px;width:340px;font-size:10px;line-height:1.3;color:var(--red)">This is place for your header text. Insert your text here, just replace this text with your own text</p>
  <div class="abs" style="left:25px;top:106px;width:430px;display:flex;gap:14px;font-size:7px;line-height:1.35;color:#aaa">
    <div style="flex:1;border-right:1px solid #ddd;padding-right:8px"><p>Lorem ipsum dolor sit amet, consectetur adipiscing elit, sed do eiusmod tempor incididunt ut labore et dolore magna aliqua. Ut enimad minim veniam, quis nostrud exercitation ullamco laboris nisi ut aliquip ex ea commodo consequat.</p><p style="margin-top:8px">Duis aute irure dolor in reprehendert in voluptate velit esse cillum dolore eu fugiat nulla pariatur excepteur.</p></div>
    <div style="flex:1;border-right:1px solid #ddd;padding-right:8px"><p>Lorem ipsum dolor sit amet, consectetur adipiscing elit, sed do eiusmod tempor incididunt ut labore et dolore magna aliqua. Ut enimad minim veniam, quis nostrud exercitation ullamco laboris nisi ut aliquip ex ea commodo consequat.</p><p style="margin-top:8px">Duis aute irure dolor in reprehendert in voluptate velit esse cillum dolore eu fugiat nulla pariatur excepteur.</p></div>
    <div style="flex:1"><p>Lorem ipsum dolor sit amet, consectetur adipiscing elit, sed do eiusmod tempor incididunt ut labore et dolore magna aliqua. Ut enimad minim veniam, quis nostrud exercitation ullamco laboris nisi ut aliquip ex ea commodo consequat.</p><p style="margin-top:8px">Duis aute irure dolor in reprehendert in voluptate velit esse cillum dolore eu fugiat nulla pariatur excepteur.</p></div>
  </div>
  <div class="foot">© Copyright 2017 QTVlink. All rights reserved.</div><div class="pg">28</div>
</section>

<section class="slide c2 r4">
  <h2 class="title">Our Team</h2>
  <div class="brand">QTVlink<i></i></div>
  <div class="photo" role="img" aria-label="Portrait photo of the CEO" style="left:183px;top:48px;width:114px;height:114px;border-radius:50%;background:radial-gradient(circle at 50% 40%,#c8d4dc,#8898a6)"></div>
  <p class="abs" style="left:0;width:478px;top:174px;text-align:center;font-size:7px;color:#666">Mr. John Smith<br><span style="color:#333">CEO</span></p>
  <p class="abs tiny" style="left:165px;width:150px;top:192px;text-align:center;font-size:5px">Lorem ipsum dolor sit amet, consectetur adipiscing elit, sed do eiusmod tempor incididunt ut labore et dolore magna aliqua. Duis aute irure dolor in reprehendert in voluptate velit esse cillum dolore eu fugiat nulla pariatur.</p>
  <div class="abs" style="left:218px;top:228px;display:flex;gap:4px"><i style="width:8px;height:8px;border-radius:50%;background:var(--red)"></i><i style="width:8px;height:8px;border-radius:50%;background:var(--red)"></i><i style="width:8px;height:8px;border-radius:50%;background:var(--red)"></i><i style="width:8px;height:8px;border-radius:50%;background:var(--red)"></i></div>
  <div class="foot">© Copyright 2017 QTVlink. All rights reserved.</div><div class="pg">29</div>
</section>

<section class="slide c3 r4">
  <h2 class="title">Monthly Subscription</h2>
  <div class="brand">QTVlink<i></i></div>
  <div class="abs" style="left:0;top:134px;width:478px;height:134px;background:var(--navy)"></div>
  <div class="abs" style="left:70px;top:90px;width:96px;height:132px;background:#fff;box-shadow:0 1px 3px rgba(0,0,0,.2);text-align:center">
    <div style="height:44px;background:var(--grey);color:#fff;padding-top:10px;font-size:16px">$300<br><span style="font-size:5px">per month</span></div>
    <div style="font-size:5px;color:#777;line-height:17.5px;padding:4px 10px">Single Edition<hr style="border:0;border-top:1px solid #ddd">30gb Cloud Service<hr style="border:0;border-top:1px solid #ddd">3 User<hr style="border:0;border-top:1px solid #ddd">Free Update</div>
  </div>
  <div class="abs" style="left:178px;top:84px;width:121px;height:146px;background:#fff;box-shadow:0 1px 3px rgba(0,0,0,.2);text-align:center">
    <div style="height:50px;background:var(--red);color:#fff;padding-top:12px;font-size:20px">$900<br><span style="font-size:5px">per month</span></div>
    <div style="font-size:5.5px;color:#777;line-height:19px;padding:4px 12px">Business Edition<hr style="border:0;border-top:1px solid #ddd">60gb Cloud Service<hr style="border:0;border-top:1px solid #ddd">8 User<hr style="border:0;border-top:1px solid #ddd">Free Update</div>
  </div>
  <div class="abs" style="left:312px;top:90px;width:96px;height:132px;background:#fff;box-shadow:0 1px 3px rgba(0,0,0,.2);text-align:center">
    <div style="height:44px;background:var(--ink);color:#fff;padding-top:10px;font-size:16px">$400<br><span style="font-size:5px">per month</span></div>
    <div style="font-size:5px;color:#777;line-height:17.5px;padding:4px 10px">Single Edition<hr style="border:0;border-top:1px solid #ddd">20gb Cloud Service<hr style="border:0;border-top:1px solid #ddd">3 User<hr style="border:0;border-top:1px solid #ddd">Free Update</div>
  </div>
</section>

<section class="slide c1 r5">
  <h2 class="title">Your Title Goes Here</h2>
  <div class="brand">QTVlink<i></i></div>
  <p class="abs" style="left:36px;top:60px;width:300px;font-size:4px;color:#aaa"><span style="color:var(--red)">Description</span> There are many variations of passages of lorem ipsum available, but the majority have suffered alteration in some form by injected humour or randomised words.</p>
  <table class="abs" style="left:32px;top:78px;width:411px;border-collapse:collapse;font-size:5.5px;color:#666;text-align:center">
    <thead style="background:var(--navy);color:#fff"><tr style="height:13px"><th style="font-weight:400">Lorem ipsum</th><th style="font-weight:400">Value</th><th style="font-weight:400">Value</th><th style="font-weight:400">Value</th><th style="font-weight:400">Value</th></tr></thead>
    <tbody>
      <tr style="height:15px;background:#f2f2f2"><td>Lorem ipsum</td><td>10</td><td>15</td><td>16</td><td>18</td></tr>
      <tr style="height:15px"><td>Lorem ipsum</td><td>12</td><td>13</td><td>15</td><td>16</td></tr>
      <tr style="height:15px;background:#f2f2f2"><td>Lorem ipsum</td><td>20</td><td>22</td><td>21</td><td>21</td></tr>
      <tr style="height:15px"><td>Lorem ipsum</td><td>10</td><td>21</td><td>12</td><td>11</td></tr>
      <tr style="height:15px;background:#f2f2f2"><td>Lorem ipsum</td><td>25</td><td>25</td><td>25</td><td>25</td></tr>
      <tr style="height:15px"><td>Lorem ipsum</td><td>10</td><td>02</td><td>51</td><td>21</td></tr>
      <tr style="height:15px;background:#f2f2f2"><td>Lorem ipsum</td><td>35</td><td>35</td><td>65</td><td>32</td></tr>
      <tr style="height:15px"><td>Lorem ipsum</td><td>26</td><td>33</td><td>35</td><td>32</td></tr>
      <tr style="height:15px;background:#f2f2f2"><td>Lorem ipsum</td><td>32</td><td>10</td><td>32</td><td>32</td></tr>
    </tbody>
  </table>
  <div class="foot">© Copyright 2017 QTVlink. All rights reserved.</div><div class="pg">31</div>
</section>

<section class="slide c2 r5">
  <h2 class="title">Our Team</h2>
  <div class="brand">QTVlink<i></i></div>
  <div class="photo" role="img" aria-label="Portrait photo of team member" style="left:30px;top:62px;width:54px;height:54px;border-radius:50%;background:linear-gradient(#c9c9c9,#7a7a7a)"></div>
  <div class="photo" role="img" aria-label="Portrait photo of team member" style="left:243px;top:62px;width:54px;height:54px;border-radius:50%;background:linear-gradient(#e0e0e0,#8a8a8a)"></div>
  <div class="photo" role="img" aria-label="Portrait photo of team member" style="left:30px;top:148px;width:54px;height:54px;border-radius:50%;background:linear-gradient(#dbe6ee,#9fb3c2)"></div>
  <div class="photo" role="img" aria-label="Portrait photo of team member" style="left:248px;top:148px;width:50px;height:54px;border-radius:50%;background:linear-gradient(#e6e6e6,#7d8fa0)"></div>
  <div class="abs" style="left:90px;top:70px;width:130px;font-size:5px;color:#888;line-height:1.3"><p style="font-size:9px;color:#444">Michael Doe</p>CEO<br><span style="color:var(--red)">MSIMPT, MBA and CIMA Dip PM</span><br>• Lorem ipsum dolor sit amet, consectetur adipiscing elit<br>• sed do eiusmod tempor incididunt ut labore et dolore magna aliqua<br>• Ut enimad minim veniam, quis nostrud exercitation</div>
  <div class="abs" style="left:300px;top:70px;width:130px;font-size:5px;color:#888;line-height:1.3"><p style="font-size:9px;color:#444">James Doe</p>Manager<br><span style="color:var(--red)">M.B.A</span><br>• Lorem ipsum dolor sit amet, consectetur adipiscing elit<br>• sed do eiusmod tempor incididunt ut labore et dolore magna aliqua<br>• Ut enimad minim veniam, quis nostrud exercitation</div>
  <div class="abs" style="left:90px;top:160px;width:130px;font-size:5px;color:#888;line-height:1.3"><p style="font-size:9px;color:#444">Jane Doe</p>Doctor of Chemistry<br><span style="color:var(--red)">M.B.A</span><br>• Lorem ipsum dolor sit amet, consectetur adipiscing elit<br>• sed do eiusmod tempor incididunt ut labore et dolore magna aliqua<br>• Ut enimad minim veniam, quis nostrud exercitation</div>
  <div class="abs" style="left:300px;top:160px;width:130px;font-size:5px;color:#888;line-height:1.3"><p style="font-size:9px;color:#444">John Doe</p>Doctor of Physical<br><span style="color:var(--red)">Professor</span><br>• Lorem ipsum dolor sit amet, consectetur adipiscing elit<br>• sed do eiusmod tempor incididunt ut labore et dolore magna aliqua<br>• Ut enimad minim veniam, quis nostrud exercitation</div>
  <div class="foot">© Copyright 2017 QTVlink. All rights reserved.</div><div class="pg">32</div>
</section>

<section class="slide c3 r5">
  <h2 class="title">Customer Testimonials</h2>
  <div class="brand">QTVlink<i></i></div>
  <div class="photo" role="img" aria-label="Portrait photo of a customer" style="left:103px;top:56px;width:64px;height:64px;border-radius:50%;background:linear-gradient(#d4d4d4,#7c7c7c)"></div>
  <p class="abs tiny" style="left:205px;top:76px;width:215px;font-size:6px">adipiscing elit, sed diam nonummy nibh euismod tincidunt ut laoreet dolore magna aliquam erat volutpat. Ut wisi enim <b style="color:#777">Lorem ipsum</b> dolor sit amet, consectetuer adipiscing elit, sed diam nonummy nibh euismod tincidunt ut laoreet dolore magna.</p>
  <div class="abs" style="left:0;top:143px;width:478px;height:125px;background:var(--navy)"></div>
  <div class="abs" style="left:129px;top:137px;width:0;height:0;border-left:6px solid transparent;border-right:6px solid transparent;border-bottom:6px solid var(--navy)"></div>
  <div class="abs" style="left:80px;top:168px;width:360px;display:flex;justify-content:space-between;color:#fff;text-align:center;font-size:5px;line-height:1.3">
    <div style="width:70px"><div style="width:36px;height:36px;border:1.5px solid #fff;border-radius:50%;margin:0 auto 8px"></div>Why does getting a loan have to be so much more complicated than ordering a fridge on ShopNest?</div>
    <div style="width:70px"><div style="width:36px;height:36px;border:1.5px solid #fff;border-radius:50%;margin:0 auto 8px"></div>Why do I have to go to a branch, fill out forms and wait for weeks to get a response?</div>
    <div style="width:70px"><div style="width:36px;height:36px;border:1.5px solid #fff;border-radius:50%;margin:0 auto 8px"></div>Why do banks refuse to lend to me despite the substantial fees I receive each month?</div>
    <div style="width:70px"><div style="width:36px;height:36px;border:1.5px solid #fff;border-radius:50%;margin:0 auto 8px"></div>Why is there no ShopNest in Banking, that identifies my needs and offers convenience at fair prices?</div>
  </div>
</section>

</div>
</body>
</html>
```